KTR Keystone Tally Resources Pty Ltd

Design a website for bookkeeping & accounting company

I like this website as an example with my own branding

https://go.lumiqor.example/sydney-bookkeeping-lp/?keyword=bookkeeping%20sydney&matchtype=e&campaignid=481726350&device=c&adgroupid=37215068492&adposition=1t1&creative=519384726105&gclid=XQzRbTpWvK7dLmN3FhJsYcGe4uA9oPiZ2wHqVxB_TkE

Number of Pages Required

1 page

Font styles to use
Sans Serif

Colors
9bcb3c

```html
<!DOCTYPE html>
<html lang="en">
<head>
<meta charset="utf-8">
<title>Keystone Tally Resources Pty Ltd</title>
<link rel="stylesheet" href="https://fonts.googleapis.com/css2?family=Raleway:wght@500;600;700&family=Open+Sans:ital,wght@0,400;0,600;0,700;1,400&display=swap">
<style>
:root{
  --green:#9bcb3c;
  --green-dark:#86b52c;
  --ink:#1c1c1c;
  --text:#6d6d6d;
  --line:#cfcfcf;
  --light:#f3f3f3;
  --white:#ffffff;
  --footer:#111111;
}
*{box-sizing:border-box;margin:0;padding:0}
html,body{width:1200px;height:3409px;overflow:hidden}
body{font-family:"Open Sans",Arial,sans-serif;color:var(--text);background:var(--white);position:relative}
.heading{font-family:"Raleway",Arial,sans-serif;color:var(--ink);font-weight:600}

/* hero */
.hero{position:absolute;left:0;top:0;width:1200px;height:672px;overflow:hidden}
.hero-photo{position:absolute;inset:0;background:linear-gradient(110deg,#2a2b2e 0%,#4b4d52 40%,#6d7076 62%,#3a3c40 100%)}
.hero-shade{position:absolute;inset:0;background:linear-gradient(90deg,rgba(0,0,0,.45),rgba(0,0,0,.1) 70%)}
.brand{position:absolute;left:98px;top:36px;display:flex;align-items:center;gap:12px;color:var(--white);font-family:"Raleway",Arial,sans-serif;font-weight:600}
.brand-mark{font-size:44px;letter-spacing:1px;line-height:1}
.brand-name{font-size:12.5px;line-height:13px;text-transform:uppercase;border-left:2px solid var(--white);padding-left:10px}
.nav{position:absolute;right:98px;top:48px;display:flex;gap:30px;align-items:center;font-family:"Raleway",Arial,sans-serif;font-weight:600;font-size:15.5px;color:var(--white)}
.nav .active{color:var(--green)}
.hero-title{position:absolute;left:98px;top:200px;font-family:"Raleway",Arial,sans-serif;font-weight:600;font-size:55px;line-height:76px;color:var(--white);letter-spacing:1px}
.btn-outline{position:absolute;left:98px;top:465px;width:185px;height:56px;border:2px solid var(--white);border-radius:28px;color:var(--white);font-family:"Raleway",Arial,sans-serif;font-weight:700;font-size:16px;display:flex;align-items:center;justify-content:center}
.slider-dots{position:absolute;left:566px;top:587px;display:flex;gap:4px}
.slider-dots span{width:12px;height:12px;border-radius:50%;border:2px solid var(--white)}
.slider-dots span.on{background:var(--white)}

.enquiry{position:absolute;left:715px;top:122px;width:386px;height:514px;background:var(--white)}
.enquiry-head{height:56px;background:var(--green);color:var(--white);font-family:"Raleway",Arial,sans-serif;font-weight:700;font-size:23px;display:flex;align-items:center;justify-content:center;letter-spacing:.5px}
.enquiry-fields{padding:16px 16px 0}
.field{height:45px;border:1px solid var(--line);margin-bottom:10px;padding:0 15px;font-size:14px;color:#555;display:flex;align-items:center}
.field.area{height:75px;align-items:flex-start;padding-top:14px}
.btn-submit{margin:18px auto 0;width:122px;height:45px;border-radius:23px;background:var(--green);color:var(--white);font-family:"Raleway",Arial,sans-serif;font-weight:700;font-size:16px;display:flex;align-items:center;justify-content:center}

/* welcome */
.welcome-title{position:absolute;left:0;width:1200px;top:765px;text-align:center;font-size:39px;line-height:50px}
.welcome-text{position:absolute;left:200px;width:800px;top:887px;text-align:center;font-size:14px;line-height:28px;color:#555}
.services{position:absolute;left:98px;top:1000px;width:1004px;display:grid;grid-template-columns:repeat(3,320px);column-gap:22px;row-gap:30px}
.service{height:280px;border:1.5px solid var(--line);text-align:center;padding-top:28px}
.service svg{width:84px;height:84px;stroke:var(--green);fill:none;stroke-width:2.4;stroke-linejoin:round;stroke-linecap:round}
.service h3{font-family:"Raleway",Arial,sans-serif;font-weight:700;font-size:18px;color:var(--ink);margin:14px 0 16px}
.service p{font-size:13.5px;line-height:26px;color:#666;padding:0 30px}
.service.featured{background:var(--green);border-color:var(--green)}
.service.featured svg{stroke:var(--white)}
.service.featured h3,.service.featured p{color:var(--white)}

/* why */
.why{position:absolute;left:0;top:1705px;width:1200px;height:553px;background:var(--light)}
.why-photo{position:absolute;left:0;top:0;width:608px;height:553px;background:linear-gradient(135deg,#cfd5dc 0%,#8e99a5 45%,#e5e8ec 80%,#b8c3cf 100%)}
.why-title{position:absolute;left:673px;top:48px;font-size:40px}
.why-text{position:absolute;left:673px;top:112px;width:440px;font-size:15px;line-height:30px;color:#777}
.reason{position:absolute;left:673px;display:flex;align-items:center;gap:30px}
.reason-icon{width:86px;height:86px;border-radius:50%;border:2px solid var(--green);display:flex;align-items:center;justify-content:center}
.reason-icon svg{width:40px;height:40px}
.reason p{font-size:17px;line-height:28px;color:var(--ink);font-weight:600}

/* partners */
.partners-title{position:absolute;left:0;width:1200px;top:2350px;text-align:center;font-size:40px}
.partners{position:absolute;left:98px;top:2450px;display:flex;gap:20px}
.partner{width:185px;height:90px;border:1.5px solid var(--line);display:flex;align-items:center;justify-content:center}
.partner span{width:120px;height:28px;background:#8a8a8a;border-radius:4px}
.arrow{position:absolute;top:2475px;width:40px;height:40px;border-radius:50%;border:1.5px solid #9a9a9a;display:flex;align-items:center;justify-content:center}

/* testimonials */
.testimonials{position:absolute;left:0;top:2636px;width:1200px;height:494px;background:linear-gradient(135deg,#a3d148,#8fc233)}
.testimonials-title{position:absolute;left:0;width:1200px;top:80px;text-align:center;color:var(--white);font-size:40px}
.quote{position:absolute;top:210px;width:307px;height:200px;border:2px solid var(--white);text-align:center;color:var(--white);padding-top:60px}
.quote p{font-style:italic;font-size:13.5px;line-height:25px;padding:0 22px}
.quote h4{font-family:"Open Sans",Arial,sans-serif;font-weight:700;font-size:17px;margin-top:8px}
.avatar{position:absolute;left:110px;top:-44px;width:86px;height:86px;border-radius:50%;border:3px solid var(--white);background:linear-gradient(160deg,#d9cbbd,#8e7f72)}

/* footer */
.footer{position:absolute;left:0;top:3130px;width:1200px;height:279px;background:var(--footer);color:#e0e0e0}
.contact{position:absolute;top:76px;display:flex;align-items:center;gap:18px;font-size:15.5px;line-height:22px}
.contact-icon{width:44px;height:44px;border-radius:50%;border:2px solid var(--green);display:flex;align-items:center;justify-content:center}
.footer-links{position:absolute;left:0;width:1200px;top:148px;text-align:center;font-size:14.5px}
.footer-links span{margin:0 12px}
.copyright{position:absolute;left:100px;top:223px;font-size:13.5px}
.social{position:absolute;right:98px;top:210px;display:flex;gap:6px}
.social span{width:38px;height:38px;border-radius:50%;border:2px solid #e0e0e0}
</style>
</head>
<body>

<header class="hero">
  <div class="hero-photo" role="img" aria-label="Photo of a business person working on a laptop showing financial charts"></div>
  <div class="hero-shade"></div>
  <div class="brand">
    <span class="brand-mark">KTR</span>
    <span class="brand-name">Keystone<br>Tally<br>Resources Pty Ltd</span>
  </div>
  <nav class="nav">
    <span class="active">HOME</span><span>SERVICES</span><span>ABOUT</span><span>CONTACT</span>
    <svg width="16" height="16" viewBox="0 0 16 16" fill="none" stroke="#fff" stroke-width="2.4"><circle cx="6.5" cy="6.5" r="4.6"/><path d="M10 10l4.5 4.5"/></svg>
  </nav>
  <h1 class="hero-title">KEYSTONE<br>TALLY<br>RESOURCES</h1>
  <div class="btn-outline">GET STARTED</div>
  <div class="slider-dots"><span class="on"></span><span></span><span></span><span></span></div>

  <form class="enquiry">
    <div class="enquiry-head">ENQUIRE NOW</div>
    <div class="enquiry-fields">
      <div class="field">Name*</div>
      <div class="field">Business Name*</div>
      <div class="field">Email*</div>
      <div class="field">Phone No*</div>
      <div class="field">No of Employees*</div>
      <div class="field area">How can we help?</div>
      <div class="btn-submit">SUBMIT</div>
    </div>
  </form>
</header>

<h2 class="heading welcome-title">WELCOME TO KEYSTONE<br>TALLY RESOURCES</h2>
<p class="welcome-text">At vero eos et accusamus et iusto odio dignissimos ducimus qui blanditiis praesentium voluptatum deleniti atque corrupti quos dolores et quas molestias excepturi sint occaecati cupiditate similique sunt in culpa qui</p>

<section class="services">
  <div class="service">
    <svg viewBox="0 0 84 84"><rect x="6" y="10" width="72" height="50" rx="3"/><rect x="12" y="16" width="60" height="38"/><path d="M36 60v10M48 60v10M28 72h28"/></svg>
    <h3>ONLINE BILL PAYMENTS</h3>
    <p>Nam libero tempore, cum soluta nobis est eligendi optio cumque nihil impedit quo minus id quod maxime placeat</p>
  </div>
  <div class="service featured">
    <svg viewBox="0 0 84 84"><rect x="4" y="20" width="76" height="44" rx="2"/><path d="M4 30a10 10 0 0 0 10-10M70 20a10 10 0 0 0 10 10M4 54a10 10 0 0 1 10 10M70 64a10 10 0 0 1 10-10"/><circle cx="42" cy="42" r="12"/><path d="M40 37l3-2v14"/></svg>
    <h3>CASH FLOW MANAGEMENT</h3>
    <p>Nam libero tempore, cum soluta nobis est eligendi optio cumque nihil impedit quo minus id quod maxime placeat</p>
  </div>
  <div class="service">
    <svg viewBox="0 0 84 84"><path d="M20 6h32l14 14v58H20z"/><path d="M52 6v14h14"/><path d="M28 30h18M28 40h30M28 50h30M28 60h30M28 70h20"/></svg>
    <h3>REPORTING</h3>
    <p>Nam libero tempore, cum soluta nobis est eligendi optio cumque nihil impedit quo minus id quod maxime placeat</p>
  </div>
  <div class="service">
    <svg viewBox="0 0 84 84"><circle cx="42" cy="22" r="10"/><circle cx="20" cy="32" r="8"/><circle cx="64" cy="32" r="8"/><path d="M26 72V52a16 16 0 0 1 32 0v20zM8 64V52a12 12 0 0 1 16-10M76 64V52a12 12 0 0 0-16-10"/></svg>
    <h3>DEBTOR MANAGEMENT</h3>
    <p>Nam libero tempore, cum soluta nobis est eligendi optio cumque nihil impedit quo minus id quod maxime placeat</p>
  </div>
  <div class="service">
    <svg viewBox="0 0 84 84"><rect x="6" y="16" width="72" height="52" rx="4"/><path d="M6 30h72M6 38h72M16 54h16M38 54h10"/></svg>
    <h3>PAYROLL SERVICES</h3>
    <p>Nam libero tempore, cum soluta nobis est eligendi optio cumque nihil impedit quo minus id quod maxime placeat</p>
  </div>
  <div class="service">
    <svg viewBox="0 0 84 84"><rect x="8" y="14" width="68" height="62" rx="3"/><path d="M8 28h68M22 8v12M42 8v12M62 8v12M8 44h68M8 60h68M25 28v48M42 28v48M59 28v48"/></svg>
    <h3>DAY TO DAY BOOKKEEPING</h3>
    <p>Nam libero tempore, cum soluta nobis est eligendi optio cumque nihil impedit quo minus id quod maxime placeat</p>
  </div>
</section>

<section class="why">
  <div class="why-photo" role="img" aria-label="Photo of hands holding a smartphone beside a laptop and printed charts"></div>
  <h2 class="heading why-title">WHY CHOOSE US</h2>
  <p class="why-text">Nam libero tempore, cum soluta nobis est eligendi optio cu mque nihil impedit quo minus id quod max..</p>
  <div class="reason" style="top:195px">
    <div class="reason-icon"><svg viewBox="0 0 40 40" fill="#9bcb3c"><circle cx="15" cy="22" r="9"/><circle cx="15" cy="22" r="3.5" fill="#f3f3f3"/><path d="M13 9h4v5h-4zM13 30h4v5h-4zM2 20h5v4H2zM23 20h5v4h-5z"/><circle cx="30" cy="11" r="6"/><circle cx="30" cy="11" r="2.2" fill="#f3f3f3"/></svg></div>
    <p>No training required -<br>we can start straight away.</p>
  </div>
  <div class="reason" style="top:305px">
    <div class="reason-icon"><svg viewBox="0 0 40 40" fill="#9bcb3c"><circle cx="20" cy="12" r="8"/><path d="M5 36a15 14 0 0 1 30 0z"/></svg></div>
    <p>We use Qualified Accountants as<br>our bookkeepers</p>
  </div>
  <div class="reason" style="top:415px">
    <div class="reason-icon"><svg viewBox="0 0 40 40" fill="none" stroke="#9bcb3c" stroke-width="2.6"><rect x="3" y="10" width="34" height="20" rx="1"/><circle cx="20" cy="20" r="5"/></svg></div>
    <p>No hidden costs. No lock ins. We have<br>a flat hourly rate</p>
  </div>
</section>

<h2 class="heading partners-title">OUR PARTNER</h2>
<div class="arrow" style="left:34px"><svg width="12" height="14" viewBox="0 0 12 14" fill="none" stroke="#555" stroke-width="2"><path d="M8 2L3 7l5 5"/></svg></div>
<div class="partners">
  <div class="partner"><span></span></div>
  <div class="partner"><span></span></div>
  <div class="partner"><span></span></div>
  <div class="partner"><span></span></div>
  <div class="partner"><span></span></div>
</div>
<div class="arrow" style="left:1126px"><svg width="12" height="14" viewBox="0 0 12 14" fill="none" stroke="#555" stroke-width="2"><path d="M4 2l5 5-5 5"/></svg></div>

<section class="testimonials">
  <h2 class="heading testimonials-title" style="color:var(--white)">TESTIMONIALS</h2>
  <div class="quote" style="left:99px">
    <div class="avatar" role="img" aria-label="Client portrait"></div>
    <p>Nam libero tempore, cum soluta nobis est eligendi optio cumque nihil impedit quo minus id quod maxime placea</p>
    <h4>Nora Blakey</h4>
  </div>
  <div class="quote" style="left:447px">
    <div class="avatar" role="img" aria-label="Client portrait"></div>
    <p>Nam libero tempore, cum soluta nobis est eligendi optio cumque nihil impedit quo minus id quod maxime placea</p>
    <h4>Tessa Rowland</h4>
  </div>
  <div class="quote" style="left:794px">
    <div class="avatar" role="img" aria-label="Client portrait"></div>
    <p>Nam libero tempore, cum soluta nobis est eligendi optio cumque nihil impedit quo minus id quod maxime placea</p>
    <h4>Owen Fairley</h4>
  </div>
</section>

<footer class="footer">
  <div class="contact" style="left:135px">
    <div class="contact-icon"><svg width="16" height="20" viewBox="0 0 16 20" fill="#9bcb3c"><path d="M8 0a7 7 0 0 0-7 7c0 5 7 13 7 13s7-8 7-13a7 7 0 0 0-7-7z"/><circle cx="8" cy="7" r="2.6" fill="#111"/></svg></div>
    <span>Larchmere Court Fenwick Row<br>KT4 7PL</span>
  </div>
  <div class="contact" style="left:418px">
    <div class="contact-icon"><svg width="18" height="18" viewBox="0 0 18 18" fill="#9bcb3c"><path d="M4 1l3 4-2 2c1 2 4 5 6 6l2-2 4 3-2 3C8 17 1 10 1 3z"/></svg></div>
    <span>1 800 555 0142</span>
  </div>
  <div class="contact" style="left:640px">
    <div class="contact-icon"><svg width="18" height="14" viewBox="0 0 18 14" fill="#9bcb3c"><rect width="18" height="14" rx="1"/><path d="M1 1l8 6 8-6" fill="none" stroke="#111" stroke-width="1.6"/></svg></div>
    <span>hello@keystonetally.example</span>
  </div>
  <div class="footer-links"><span>Help</span>|<span>FAQ</span>|<span>Support</span>|<span>Sitemap</span>|<span>Terms Of Use</span>|<span>Privacy Statement</span></div>
  <p class="copyright">Copyrights © 2018, Keystone Tally Resources. All rights reserved.</p>
  <div class="social"><span></span><span></span><span></span><span></span></div>
</footer>

</body>
</html>
```